Design some business cards and letterhead

Hi,

I need some business cards and letterhead designed for my company. The letterhead that is designed must be able to be typed on in MSword. My website is [login to view URL] and the blue can be seen on the website.

I am trying to rebrand the company and give it a modern look and feel and have attached the colour schemes of some sample stationary i found.

I need:
The logo attached to be made into two additional versions - A green and a pink/ red version as per attached sample
Business card design for 2 people
Letterhead design incorporating colour scheme

```html
<!DOCTYPE html>
<html lang="en">
<head>
<meta charset="utf-8">
<title>KDC Business Card</title>
<link href="https://fonts.googleapis.com/css2?family=Open+Sans:wght@400;600;700;800&display=swap" rel="stylesheet">
<style>
  :root {
    --brand-blue: #1b8fd6;
    --brand-blue-dark: #1479bd;
    --faint-blue: #e1ecf7;
    --accent-yellow: #f2d21b;
    --accent-red: #e0245e;
    --accent-green: #8cc63f;
    --ink: #2b2b2b;
    --rule: #9a9a9a;
    --card-white: #ffffff;
    --backdrop: #eeeeee;
  }
  * { box-sizing: border-box; margin: 0; padding: 0; }
  html, body {
    width: 1200px; height: 900px; overflow: hidden;
    background: var(--backdrop);
    font-family: "Open Sans", Arial, sans-serif;
  }
  .stage {
    position: relative; width: 1200px; height: 900px;
    display: flex; flex-direction: column; align-items: center; justify-content: center; gap: 50px;
  }
  .card {
    position: relative; width: 680px; height: 378px; overflow: hidden;
    box-shadow: 0 6px 18px rgba(0,0,0,0.15);
  }
  .accent-strip {
    position: absolute; left: 0; right: 0; bottom: 0; height: 8px; display: flex;
  }
  .accent-strip span { display: block; height: 100%; }
  .accent-strip .yellow { background: var(--accent-yellow); width: 200px; }
  .accent-strip .red { background: var(--accent-red); width: 200px; }
  .accent-strip .green { background: var(--accent-green); width: 150px; }
  .accent-strip .blue { background: var(--brand-blue-dark); flex: 1; }

  /* Front */
  .card-front { background: var(--brand-blue); }
  .front-brand {
    position: absolute; left: 0; right: 0; top: 88px; text-align: center; color: var(--card-white);
  }
  .front-brand .wordmark {
    font-size: 130px; font-weight: 800; line-height: 1; letter-spacing: 2px;
  }
  .front-brand .tagline {
    margin-top: 10px; font-size: 19px; font-weight: 700; letter-spacing: 1px;
  }

  /* Back */
  .card-back { background: var(--card-white); }
  .back-wordmark {
    position: absolute; left: 36px; top: 30px;
    font-size: 78px; font-weight: 800; line-height: 1; color: var(--brand-blue);
  }
  .faint-wordmark {
    position: absolute; right: -30px; top: 140px;
    font-size: 230px; font-weight: 800; line-height: 1; color: var(--faint-blue);
  }
  .edge-tab {
    position: absolute; right: 0; top: 140px; width: 9px; height: 42px;
    background: var(--brand-blue); border-radius: 5px 0 0 5px;
  }
  .person {
    position: absolute; right: 40px; top: 142px; text-align: right;
  }
  .person .name { font-size: 22px; font-weight: 700; color: var(--brand-blue); }
  .person .role { font-size: 15px; color: var(--ink); margin-top: 2px; }
  .divider {
    position: absolute; left: 36px; top: 196px; width: 440px; height: 1px; background: var(--rule);
  }
  .contacts {
    position: absolute; left: 36px; top: 248px; list-style: none;
    font-size: 15px; color: var(--ink);
  }
  .contacts li { display: flex; align-items: center; height: 23px; }
  .contacts svg { width: 14px; height: 14px; margin-right: 10px; fill: var(--brand-blue); flex: none; }
  .contacts em { font-size: 13px; margin-left: 4px; }
  .web-tab {
    position: absolute; right: 0; bottom: 0; width: 150px; height: 30px;
    background: var(--brand-blue); border-top-left-radius: 14px;
    color: var(--card-white); font-size: 14px; display: flex; align-items: center; justify-content: center;
  }
  .web-tab b { font-weight: 700; }
</style>
</head>
<body>
<main class="stage">
  <section class="card card-front">
    <div class="front-brand">
      <div class="wordmark">KDC</div>
      <div class="tagline">Kestrel Data &amp; Communications</div>
    </div>
    <div class="accent-strip"><span class="yellow"></span><span class="red"></span><span class="green"></span><span class="blue"></span></div>
  </section>

  <section class="card card-back">
    <div class="faint-wordmark" aria-hidden="true">KDC</div>
    <div class="back-wordmark">KDC</div>
    <div class="edge-tab"></div>
    <div class="person">
      <div class="name">Liam Hartley</div>
      <div class="role">Manager - ICT services</div>
    </div>
    <div class="divider"></div>
    <ul class="contacts">
      <li><svg viewBox="0 0 16 16"><path d="M3.6 1.2l2.2 2.6c.4.5.4 1.1 0 1.6L4.6 6.7c.9 2 2.6 3.7 4.7 4.7l1.3-1.2c.5-.4 1.1-.4 1.6 0l2.6 2.2c.5.4.5 1.1.1 1.5l-1.3 1.3C11.2 17 .2 6 1.6 3.7L2.1 2.4c.4-.6 1.1-.8 1.5-1.2z"/></svg>98 000 111 222</li>
      <li><svg viewBox="0 0 16 16"><path d="M4.5 0h7c.8 0 1.5.7 1.5 1.5v13c0 .8-.7 1.5-1.5 1.5h-7C3.7 16 3 15.3 3 14.5v-13C3 .7 3.7 0 4.5 0zM5 2v10h6V2H5zm3 11a1 1 0 100 2 1 1 0 000-2z"/></svg>0400 000 123</li>
      <li><svg viewBox="0 0 16 16"><path d="M1 3h14v10H1V3zm1.5 1.3v.3L8 8.6l5.5-4v-.3h-11zm11 2L8 10.2 2.5 6.3v5.4h11V6.3z"/></svg>sales@kdc.example<em>(sales)</em></li>
      <li><svg viewBox="0 0 16 16"><path d="M1 3h14v10H1V3zm1.5 1.3v.3L8 8.6l5.5-4v-.3h-11zm11 2L8 10.2 2.5 6.3v5.4h11V6.3z"/></svg>Support@kdc.example<em>(support)</em></li>
    </ul>
    <div class="accent-strip"><span class="yellow"></span><span class="red"></span><span class="green"></span><span class="blue"></span></div>
    <div class="web-tab">www.<b>kdc</b>.example</div>
  </section>
</main>
</body>
</html>
```